Professional & attention grabbing.

A business card design, front and back. I already have a logo I will attach, but I am open to something new as well.
Things to include:
Name:
Title:
Phone:
Email:
Wanting something that is professional but attention grabbing.
Also we do a lot of work using drones on natural gas pipelines (leading the future)if you want to include any of that. I'm open to ideas.
Target Market(s)
Natural gas transmission industry / greenhouse gas mitigation industry
Industry/Entity Type
Business
Contact Information for Business Card
All details have been conveyed above.
Colors
Designer to choose colors to be used in the design.
Look and feel
Each slider illustrates characteristics of the customer's brand and the style your logo design should communicate.

```html
<!DOCTYPE html>
<html lang="en">
<head>
<meta charset="utf-8">
<title>Kestrel Line Inspections – Business Card</title>
<link rel="stylesheet" href="https://fonts.googleapis.com/css2?family=Open+Sans:wght@400;600;700&display=swap">
<style>
  :root {
    --ink: #0b0c10;
    --paper: #ffffff;
    --brand-red: #be1e24;
    --brand-grey: #3a3a3c;
    --muted: #3d3e42;
    --light: #f2f2f2;
    --icon-grey: #8a8b8e;
  }
  * { margin: 0; padding: 0; box-sizing: border-box; }
  html, body { width: 1007px; height: 1200px; overflow: hidden; background: var(--paper); }
  body { position: relative; font-family: "Open Sans", sans-serif; }

  .card { position: absolute; left: 0; width: 1007px; background: var(--ink); }
  .card--front { top: 0; height: 578px; }
  .card--back { top: 621px; height: 579px; }

  .front-panel {
    position: absolute; left: 72px; top: 73px; width: 863px; height: 432px;
    background: var(--paper);
    display: flex; align-items: center; justify-content: center; gap: 22px;
  }
  .brand-square { width: 58px; height: 58px; background: var(--brand-red); flex: none; }
  .brand-name {
    font-weight: 700; font-size: 44px; letter-spacing: 0.5px;
    color: var(--brand-grey); white-space: nowrap;
  }

  .back-panel { position: absolute; left: 0; top: 0; width: 1007px; height: 579px; display: block; }

  .company {
    position: absolute; left: 84px; top: 682px;
    font-weight: 700; font-size: 41px; letter-spacing: 0.3px; line-height: 1.2;
    color: var(--brand-red);
  }
  .person {
    position: absolute; left: 84px; top: 742px;
    font-size: 22px; color: var(--muted);
  }
  .person .role { color: var(--light); }

  .contacts { position: absolute; left: 86px; top: 954px; list-style: none; }
  .contact { display: flex; align-items: center; height: 40px; margin-bottom: 17px; }
  .contact-icon { width: 40px; height: 40px; flex: none; margin-right: 14px; }
  .contact-text { font-size: 29px; color: var(--light); }

  .back-brand {
    position: absolute; left: 755px; top: 910px;
    display: flex; align-items: center; gap: 12px;
    transform: translate(-50%, -50%) rotate(66deg);
    white-space: nowrap;
  }
  .back-brand .brand-square { width: 30px; height: 30px; }
  .back-brand .brand-name { font-size: 27px; }
</style>
</head>
<body>
  <section class="card card--front">
    <div class="front-panel">
      <span class="brand-square"></span>
      <span class="brand-name">KESTREL LINE INSPECTIONS</span>
    </div>
  </section>

  <section class="card card--back">
    <svg class="back-panel" width="1007" height="579" viewBox="0 0 1007 579">
      <polygon points="502,73 935,73 935,505 686,505" fill="#ffffff"/>
    </svg>
  </section>

  <div class="back-brand">
    <span class="brand-square"></span>
    <span class="brand-name">KESTREL LINE INSPECTIONS</span>
  </div>

  <h1 class="company">EMPRESANOME</h1>
  <p class="person">Lucas Ferreira <span class="role">Designer</span></p>

  <ul class="contacts">
    <li class="contact">
      <svg class="contact-icon" viewBox="0 0 40 40">
        <circle cx="20" cy="20" r="18.5" fill="none" stroke="var(--icon-grey)" stroke-width="2.5"/>
        <path d="M14 11 l4 0 l1.5 5 l-2.5 2 q2 4 5 6 l2-2.5 l5 1.5 l0 4 q-1 2 -4 2 q-8 -1 -12 -11 q-1 -5 1 -7z" fill="none" stroke="var(--icon-grey)" stroke-width="2" stroke-linejoin="round"/>
      </svg>
      <span class="contact-text">(00) 000000-0000</span>
    </li>
    <li class="contact">
      <svg class="contact-icon" viewBox="0 0 40 40">
        <circle cx="20" cy="20" r="18.5" fill="none" stroke="var(--icon-grey)" stroke-width="2.5"/>
        <rect x="10" y="13" width="20" height="14" fill="none" stroke="var(--icon-grey)" stroke-width="2"/>
        <path d="M10 13 l10 8 l10 -8 M10 27 l7 -6 M30 27 l-7 -6" fill="none" stroke="var(--icon-grey)" stroke-width="2"/>
      </svg>
      <span class="contact-text">email@gmil.com</span>
    </li>
    <li class="contact">
      <svg class="contact-icon" viewBox="0 0 40 40">
        <circle cx="20" cy="20" r="18.5" fill="none" stroke="var(--icon-grey)" stroke-width="2.5"/>
        <path d="M20 32 q-9 -10 -9 -15 a9 9 0 0 1 18 0 q0 5 -9 15z" fill="var(--icon-grey)"/>
        <circle cx="20" cy="17" r="3.5" fill="var(--ink)"/>
      </svg>
      <span class="contact-text">&nbsp;End</span>
    </li>
  </ul>
</body>
</html>
```